One pager fact sheet for healthcare companies

We are looking for a designer to create a theme based off this example. The project will consist of building a layout and theme for a one page, front and back handout. The handout will be used as part of an educational series for medical professionals. The format must be suitable for print production. The theme should be clear, concise, and professional. Cluttered graphics will not be useable.
This project has potential to include additional work over the next 3 months.

Target Market(s)

Healthcare professionals

Industry/Entity Type

Healthcare

Font styles to use
Serif
Sans Serif

Requirements
Must have
• A professional look and feel
Should not have
• Cluttered graphics or busy look

```html
<!DOCTYPE html>
<html lang="en">
<head>
<meta charset="utf-8">
<title>Educational Series – Health System Fact Sheet</title>
<link href="https://fonts.googleapis.com/css2?family=Fira+Sans:wght@400;500;600;700&display=swap" rel="stylesheet">
<style>
:root{
  --blue:#3f97d6;
  --title-blue:#1f74ba;
  --ink:#1c1c1c;
  --text:#2b2b2b;
  --paper:#fbfbfb;
  --white:#ffffff;
}
*{margin:0;padding:0;box-sizing:border-box}
html,body{width:927px;height:1200px;overflow:hidden}
body{
  position:relative;background:var(--paper);
  font-family:"Fira Sans",Arial,sans-serif;color:var(--text);
  font-size:13px;line-height:16.3px;
}
.hero{position:absolute;left:0;top:0;width:927px;height:127px;
  background:linear-gradient(90deg,#f1f4f7 0%,#e6ecf2 40%,#b9c6d3 62%,#6c7f93 82%,#495b6e 100%)}
.series-title{position:absolute;left:50px;top:32px;font-size:28px;line-height:30px;font-weight:600;color:var(--title-blue);letter-spacing:-.2px}
.series-sub{position:absolute;left:50px;top:64px;height:28px;padding:0 8px;background:var(--blue);color:var(--white);font-size:18px;line-height:28px;font-weight:400}
.section-tab{position:absolute;height:35px;background:var(--blue);color:var(--white);font-weight:600;font-size:16.5px;line-height:35px;padding-left:14px}
.section-rule{position:absolute;height:2px;background:var(--blue)}
.block{position:absolute}
.block p{margin:0}
b,.label{font-weight:600;color:var(--ink)}
.justify{text-align:justify}
.dist{width:311px}
.dist-row{display:flex;justify-content:space-between}
.plans{display:flex}
.plans ul{list-style:none;width:146px}
.footer{position:absolute;left:0;top:1132px;width:927px;height:68px;background:var(--blue);color:var(--white);text-align:center;font-size:13px;line-height:16px;padding-top:21px}
.footer b{color:var(--white)}
</style>
</head>
<body>
<div class="hero" role="img" aria-label="Photograph of two smiling medical professionals reviewing work together"></div>
<div class="series-title">EDUCATIONAL SERIES</div>
<div class="series-sub">FOR MEDICAL PROFESSIONALS</div>

<div class="section-tab" style="left:78px;top:195px;width:111px">KEY FACTS</div>
<div class="section-rule" style="left:78px;top:228px;width:333px"></div>
<div class="block" style="left:78px;top:250px;width:340px">
  <p><span class="label">Organization Type:</span>&nbsp;&nbsp; Not for Profit Health System</p>
  <p style="margin-top:15.7px"><span class="label">Leadership Team and Contact Information:</span></p>
  <p style="margin-top:15.7px">• <b>Helen R. Carver</b>, CEO</p>
  <p>• <b>Marcus D. Whitfield, II</b>, President</p>
  <p>• <b>Thomas E. Albrecht</b>, EVP and COO</p>
  <p>• <b>Daniel Okafor, Jr.</b> MD, EVP and Chief Medical Officer</p>
  <p style="margin-top:19.7px"><span class="label">Physicians in Network:</span></p>
  <p style="margin-top:15.7px"><b>Total:</b> 2,400 Salaried, 3,000 Affiliated</p>
  <p><b>PCPs</b>: 1,000 Salaried, 1,500 Affiliated</p>
  <p><b>Ophthalmologists:</b> 35 Salaried, 0 Affiliated</p>
  <p><b>Retina Specialists:</b> 10 Salaried, 0 Affiliated</p>
  <p style="margin-top:15.7px"><span class="label">Covered Lives:</span>&nbsp;&nbsp;&nbsp; 800,000</p>
</div>

<div class="section-tab" style="left:532px;top:195px;width:180px">SYSTEM STRUCTURE</div>
<div class="section-rule" style="left:532px;top:228px;width:319px"></div>
<div class="block justify" style="left:532px;top:250px;width:307px">
  <p style="text-align:left"><span class="label">Geographic Coverage:</span>&nbsp; Michigan</p>
  <p style="margin-top:13.7px;text-align:left"><span class="label">Number of Hospitals and Facilities</span></p>
  <p style="margin-top:14.7px">• 7 Hospitals</p>
  <p>• Over 35 medical centers and facilities across multiple counties in Michigan</p>
  <p style="margin-top:17.7px;text-align:left"><span class="label">Key Affiliations</span></p>
  <p style="margin-top:14px">• Medical Group has more than 1,100 physicians that staff LC hospital, Cedar Ridge hospital, and 26 medical centers</p>
  <p>• Physician Network is a physician-led subsidiary, comprising the Medical Group, hospital-employed and private practice physicians</p>
  <p>• 2,000 affiliated private practice physicians</p>
</div>

<div class="section-tab" style="left:78px;top:564px;width:104px">SERVICES</div>
<div class="section-rule" style="left:78px;top:597px;width:772px"></div>
<div class="block" style="left:78px;top:618px;width:318px">
  <p><span class="label">Key Services and Facilities</span></p>
  <p style="margin-top:19.7px"><b>Major service lines:</b> cardiac care, women’s and children’s services, cancer care, orthopedics, transplants, neuroscience, trauma, and urology</p>
  <p><b>Key Facilities:</b> ClearView Eye centers include offices for ophthalmologists and retina specialists</p>
</div>
<div class="block dist" style="left:532px;top:618px">
  <p><span class="label">Distribution of Outpatient Services</span></p>
  <div class="dist-row" style="margin-top:19.7px"><span>In Facilities:</span><span>40%</span></div>
  <div class="dist-row"><span>In Owned Practices:</span><span>30%</span></div>
  <div class="dist-row"><span>In Affiliated Practices:</span><span>20%</span></div>
  <div class="dist-row"><span>Unaffiliated/ Out of Network:</span><span>10%</span></div>
</div>

<div class="section-tab" style="left:78px;top:770px;width:413px">KEY PAYER RELATIONSHIPS AND PAYMENT MODELS</div>
<div class="section-rule" style="left:78px;top:803px;width:772px"></div>
<div class="block" style="left:78px;top:829px">
  <p><span class="label">Key Plans</span></p>
  <div class="plans" style="margin-top:14px">
    <ul><li>• Palomera Health</li><li>• Brightwater Mutual</li><li>• Tallowmere Network</li><li>• Quillon Plans</li><li>• Orrinvale</li></ul>
    <ul><li>• Medicare</li><li>• Michigan Medicaid</li><li>• Vantrell Care</li><li>• Ashgrove Health</li><li>• Corvena Health</li></ul>
  </div>
</div>
<div class="block justify" style="left:504px;top:829px;width:351px">
  <p style="text-align:left"><span class="label">Level of Risk Taken</span></p>
  <p style="margin-top:13px">• 80% of revenue is billed under a risk-based payment scheme</p>
  <p>• Half of these lives include the risk for outpatient, physician-administered biologics</p>
</div>
<div class="block" style="left:82px;top:969px;width:778px">
  <p>• COMPANY accepts a variety of risk-based payment models including full and partial risk, bundled payments, and ACO contracts.</p>
  <p>• All decisions to join an ACO or participate in a risk-based contract are made at the corporate level.</p>
  <p>• COMPANY is contracted with CMS as a Next Generation ACO. Through the HMO product, this contract represents 30% of the health system’s revenue and covers over 20,000 Medicare lives.</p>
  <p>• The remaining share of revenue typically includes a value-based payment model. Contracts with private payers, such as Brightwater Mutual, incorporate contracts based on performance and quality of care which may lead to bonus payments.</p>
</div>

<footer class="footer"><b>Contact Information:</b> For additional information, please contact us at:</footer>
</body>
</html>
```